Webpage

I am a professional genealogist. I need a webpage that is professional looking (using the logo I chose), I can add hyperlinks and photos to if and when I want.

```html
<!DOCTYPE html>
<html lang="en">
<head>
<meta charset="utf-8">
<title>Lineage Research Services</title>
<link rel="stylesheet" href="https://fonts.googleapis.com/css2?family=Arimo:wght@400;700&family=Roboto:wght@300;400;700&display=swap">
<style>
:root{
  --teal:#13aabf;
  --orange:#f39a1b;
  --ink:#333;
  --band:#404040;
  --footer:#0b0b0b;
  --white:#fff;
}
*{box-sizing:border-box;margin:0;padding:0}
html,body{width:1200px;height:900px;overflow:hidden;background:var(--white);font-family:"Arimo",Arial,sans-serif;color:var(--ink)}
.page{position:absolute;left:194px;top:0;width:812px;height:882px}
a{color:inherit;text-decoration:none}

/* header */
.site-header{position:absolute;left:0;top:0;width:812px;height:68px;background:var(--white);border-bottom:3px solid #e6e6e6}
.brand{position:absolute;left:118px;top:10px;display:flex;align-items:center;gap:7px}
.brand-dot{width:38px;height:38px;border-radius:50%;background:#8fd3c8}
.brand-name{font-size:13px;color:#3d4a55;font-weight:400;line-height:14px;display:flex;flex-direction:column;align-items:flex-end}
.home-icon{position:absolute;left:292px;top:28px}
.main-nav a{position:absolute;top:29px;font-size:7px;letter-spacing:.4px;color:#444;white-space:nowrap;line-height:8px}
.nav-sep{position:absolute;top:28px;width:1px;height:9px;background:#999}
.login-btn{position:absolute;left:608px;top:25px;width:49px;height:17px;background:var(--teal);color:#fff;font-size:8px;font-weight:700;text-align:center;line-height:17px;border-radius:2px}
.cart{position:absolute;left:667px;top:27px}
.cart-count{position:absolute;left:677px;top:16px;width:16px;height:16px;border-radius:50%;background:var(--orange);color:#fff;font-size:8px;text-align:center;line-height:16px}

/* hero */
.hero{position:absolute;left:0;top:68px;width:812px;height:289px;background:linear-gradient(100deg,#e9e1d9 0%,#d9b8a0 30%,#c79a7e 55%,#e8ddd5 80%,#f3efea 100%)}
.hero-card{position:absolute;left:117px;top:80px;width:309px;height:142px;background:rgba(19,170,191,.88);padding:22px 20px}
.hero-card h1{color:#fff;font-size:12.5px;font-weight:700;line-height:15px;text-transform:uppercase;width:270px}
.hero-btn{position:absolute;left:20px;top:80px;width:113px;height:26px;background:#fff;color:var(--teal);font-size:9px;letter-spacing:.5px;text-align:center;line-height:26px}

/* service tabs */
.service-tabs{position:absolute;left:0;top:357px;width:812px;height:58px;background:linear-gradient(#ececea,#d6d6d4)}
.tab{position:absolute;top:0;width:110px;height:58px;text-align:center;font-size:7px;line-height:8.5px;letter-spacing:.3px;color:#333;padding-top:10px}
.tab svg{display:block;margin:0 auto 4px}
.tab.active{width:114px;background:#f3f3f3;border-top:3px solid var(--teal);color:var(--teal);padding-top:7px}
.tab.active::before{content:"";position:absolute;left:50%;top:-9px;margin-left:-6px;border:6px solid transparent;border-bottom-color:var(--teal);border-top:none}

/* content */
.intro{position:absolute;left:0;top:415px;width:812px;height:230px;background:#fafafa}
.intro h2{position:absolute;left:117px;top:21px;font-family:"Roboto",Arial,sans-serif;font-weight:300;font-size:12.5px;letter-spacing:.4px;color:#666}
.intro-rule{position:absolute;left:117px;top:43px;width:569px;height:1px;background:#d3d3d3}
.intro p{position:absolute;left:117px;top:51px;width:330px;font-size:8px;line-height:11.2px;color:#444;text-align:justify}
.intro-photo{position:absolute;left:462px;top:54px;width:224px;height:140px;background:linear-gradient(120deg,#f2f1ee,#dcd6cc 55%,#c9c3ba)}

/* clients */
.clients{position:absolute;left:0;top:645px;width:812px;height:79px;background:var(--band)}
.clients-tag{position:absolute;left:364px;top:-7px;width:77px;height:17px;background:#0b0b0b;color:#fff;font-size:7.5px;font-weight:700;text-align:center;line-height:17px;border-radius:2px 2px 0 0}
.client-list{position:absolute;left:112px;top:34px;width:590px;display:flex;justify-content:space-between;list-style:none}
.client-list li{font-size:11px;color:#8a8a8a;font-weight:700;width:80px;text-align:center}

/* footer */
.site-footer{position:absolute;left:0;top:724px;width:812px;height:129px;background:var(--footer);color:#ddd}
.footer-col{position:absolute;top:16px;font-size:7px;line-height:9px}
.footer-col h3{font-family:"Roboto",Arial,sans-serif;font-size:9.5px;font-weight:700;color:#fff;margin-bottom:9px}
.col-about{left:110px;width:170px}
.col-about strong{display:block;font-size:8.5px;color:#fff}
.col-about address{font-style:normal;margin-top:9px}
.col-tweet{left:319px;width:170px}
.col-tweet h3.follow{margin-top:14px;margin-bottom:6px}
.social{display:flex;gap:2px}
.social span{width:12px;height:12px;border-radius:50%;background:#5a5a5a}
.col-news{left:522px;width:180px}
.news-form{position:absolute;left:0;top:70px;display:flex;gap:4px}
.news-input{width:124px;height:16px;background:#cfcfcf;border-radius:2px;font-size:7px;color:#444;padding:4px 7px}
.news-btn{width:53px;height:16px;background:var(--teal);color:#fff;font-size:9px;font-weight:700;text-align:center;line-height:16px;border-radius:2px}

.legal-bar{position:absolute;left:0;top:853px;width:812px;height:29px;background:var(--teal);color:#fff;font-size:6.5px}
.legal-bar .copy{position:absolute;left:113px;top:11px}
.legal-links{position:absolute;right:108px;top:10px;display:flex;gap:9px}
.legal-links a.current{text-decoration:underline}
</style>
</head>
<body>
<div class="page">
  <header class="site-header">
    <a class="brand" href="#"><span class="brand-dot"></span><span class="brand-name"><span>Lineage Research</span><span>Services</span></span></a>
    <svg class="home-icon" width="11" height="10" viewBox="0 0 11 10"><path d="M5.5 0L0 5h1.5v5h3V7h2v3h3V5H11z" fill="#13aabf"/></svg>
    <nav class="main-nav">
      <a href="#" style="left:317px">ABOUT US</a>
      <span class="nav-sep" style="left:363px"></span>
      <a href="#" style="left:375px">SERVICES</a>
      <span class="nav-sep" style="left:423px"></span>
      <a href="#" style="left:434px">PUBLICATIONS</a>
      <span class="nav-sep" style="left:492px"></span>
      <a href="#" style="left:507px">BLOG</a>
      <span class="nav-sep" style="left:537px"></span>
      <a href="#" style="left:549px">CONTACT US</a>
    </nav>
    <a class="login-btn" href="#">Login</a>
    <svg class="cart" width="15" height="13" viewBox="0 0 15 13"><path d="M0 1h3l2 7h8l2-5H4" fill="none" stroke="#13aabf" stroke-width="1.6"/><circle cx="6" cy="11" r="1.4" fill="#13aabf"/><circle cx="12" cy="11" r="1.4" fill="#13aabf"/></svg>
    <span class="cart-count">3</span>
  </header>

  <section class="hero" role="img" aria-label="Photo of a smiling family of four relaxing together on a sofa">
    <div class="hero-card">
      <h1>When it comes to your family history, there is always something new to learn.</h1>
      <a class="hero-btn" href="#">LEARN MORE</a>
    </div>
  </section>

  <nav class="service-tabs">
    <a class="tab" href="#" style="left:101px"><svg width="16" height="16" viewBox="0 0 16 16"><circle cx="8" cy="8" r="7" fill="#333"/><rect x="4" y="9" width="8" height="3" fill="#ddd"/></svg>FORENSIC<br>GENEALOGY</a>
    <a class="tab" href="#" style="left:228px"><svg width="16" height="16" viewBox="0 0 16 16"><circle cx="8" cy="8" r="6.5" fill="none" stroke="#333" stroke-width="1.5"/><circle cx="8" cy="7" r="2.5" fill="#333"/><rect x="7.2" y="8" width="1.6" height="6" fill="#333"/></svg>KINSHIP<br>DETERMINATION</a>
    <a class="tab active" href="#" style="left:367px"><svg width="18" height="18" viewBox="0 0 18 18"><circle cx="9" cy="9" r="7.5" fill="none" stroke="#13aabf" stroke-width="2"/><circle cx="9" cy="9" r="3" fill="#13aabf"/></svg>RESEARCH ANALYSIS<br>&amp; CONSULTATION</a>
    <a class="tab" href="#" style="left:504px"><svg width="16" height="16" viewBox="0 0 16 16"><circle cx="8" cy="8" r="6" fill="none" stroke="#333" stroke-width="2.5" stroke-dasharray="2 1.5"/></svg>TEXAS<br>RESEARCHER</a>
    <a class="tab" href="#" style="left:613px"><svg width="18" height="18" viewBox="0 0 18 18"><circle cx="9" cy="9" r="8" fill="none" stroke="#333" stroke-width="1.4"/><path d="M9 3v12M3 9h12M5 5l8 8M13 5l-8 8" stroke="#333" stroke-width="1.6"/></svg>RECORD<br>RETRIEVAL</a>
  </nav>

  <section class="intro">
    <h2>PROFESSIONAL GENEALOGISTS</h2>
    <div class="intro-rule"></div>
    <p>Lorem ipsum dolor sit amet, consectetuer adipiscing elit, sed diam nonummy nibh euismod tincidunt ut laoreet dolore magna aliquam erat volutpat. Ut wisi enim ad minim veniam, quis nostrud exerci tation ullamcorper suscipit lobortis nisl ut aliquip ex ea commodo consequat. Duis autem vel eum iriure dolor in hendrerit in vulputate velit esse molestie consequat, vel illum dolore eu feugiat nulla facilisis at vero eros et accumsan et iusto odio dignissim qui blandit praesent luptatum zzril delenit augue duis dolore te feugait nulla facilisi. Nam liber tempor cum soluta nobis eleifend option congue nihil imperdiet doming id quod mazim placerat facer possim assum. Typi non habent claritatem insitam; est usus legentis in iis qui facit eorum claritatem. Investigationes demonstraverunt lectores legere me lius quod ii legunt saepius. Claritas est etiam processus dynamicus, qui sequitur mutationem consuetudium lectorum. Mirum est notare quam littera gothica, quam nunc putamus parum claram, anteposuerit litterarum formas humanitatis per seacula quarta decima et quinta decima. Eodem modo typi, qui nunc nobis videntur parum clari, fiant sollemnes in futurum.</p>
    <div class="intro-photo" role="img" aria-label="Photo of two colleagues working together at a desk in a bright office"></div>
  </section>

  <section class="clients">
    <span class="clients-tag">Our Clients</span>
    <ul class="client-list">
      <li>Northgate</li><li>Bellcourt</li><li>Harwick</li><li>Ostler</li><li>Pemberly</li><li>Quillon</li>
    </ul>
  </section>

  <footer class="site-footer">
    <div class="footer-col col-about">
      <h3>ABOUT</h3>
      <strong>Lineage Research Services</strong>
      consectetur mi vitae est. Mauris placerat eleifend leo. Ultricies eget, tempor sit amet, ante.
      <address>Dana Whitfield, Professional Genealogist<br>PO Box 4471<br>Austin, TX 78701-4471<br>512-555-0148</address>
    </div>
    <div class="footer-col col-tweet">
      <h3>Latest tweet</h3>
      @ info Lorem ipsum dolor sit amet, consectetur adipiscing elit. Nam fringilla eros! -elit. Nam fringilla eros!about 10h ago.
      <h3 class="follow">Follow us</h3>
      <div class="social"><span></span><span></span><span></span><span></span></div>
    </div>
    <div class="footer-col col-news">
      <h3>NewsLetter</h3>
      Subscribe to our newsletter and get latest news and exclusive offers straight to your inbox. No spam, we promise. You can unsubscribe anytime.
      <div class="news-form"><span class="news-input">Your e-mail here..</span><span class="news-btn">Subscribe</span></div>
    </div>
  </footer>

  <div class="legal-bar">
    <span class="copy">Copyright © 2014 lineageresearch.example. All rights reserved.</span>
    <div class="legal-links"><a class="current" href="#">Terms of Service</a><a href="#">Privacy Policy</a><a href="#">Earnings Disclaimer</a></div>
  </div>
</div>
</body>
</html>
```